Food home delivery flyer to attract new customers and drive web traffic

We need a flyer for Grubella Home Delivery for our door to door leaflet drop. The aim of our marketing is to attract new customers by driving traffic to our website and raise awareness of our service.

We want the flyer in A5, double sided, and in colour. This campaign will be primarily in print, but we need a PDF option also.

Please visit www.grubellahomedelivery.example to obtain a real feel of who we are and what we do.

The flyer should contain the Grubella Home Delivery logo, with our images to compliment our service and what we offer. All are attached to this brief, along with what wording we expect to be included in the flyer.

The main points we need to shout about are:
Sourcing fresh produce from local growers
Partnering with local businesses
Friendly team offering superior customer service
Fast, safe home delivery
Sustainable business

```html
<!DOCTYPE html>
<html lang="en">
<head>
<meta charset="utf-8">
<title>Grubella Home Delivery – A5 Flyer</title>
<link rel="stylesheet" href="https://fonts.googleapis.com/css2?family=Poppins:ital,wght@0,400;0,500;0,600;0,700;1,400;1,600;1,700&family=Caveat+Brush&display=swap">
<style>
  :root{
    --leaf:#8cba3b;
    --forest:#0f5a2a;
    --forest-line:#0c5226;
    --logo-green:#1e6b33;
    --ink:#1a1a1a;
    --paper:#ffffff;
    --backdrop:#e4e4e4;
    --produce-a:#7f9a3a;
    --produce-b:#c8542c;
  }
  *{box-sizing:border-box;margin:0;padding:0}
  html,body{width:1200px;height:1101px;overflow:hidden}
  body{background:var(--backdrop);font-family:"Poppins",Arial,sans-serif;position:relative;color:var(--ink)}
  .flyer{position:absolute;top:213px;width:458px;height:652px;overflow:hidden}
  .abs{position:absolute}
  .stripes{background:var(--forest) repeating-linear-gradient(to bottom,transparent 0 6px,var(--forest-line) 6px 7px)}
  .script{font-family:"Caveat Brush",cursive;color:var(--paper)}
  .quote-mark{font-family:Georgia,serif;font-weight:700;line-height:1}

  /* front */
  .front{left:131px;background:var(--paper)}
  .front .hero-shape{left:0;top:0}
  .front .brand{left:270px;top:30px;width:150px;text-align:right;color:var(--logo-green);font-weight:500;line-height:1}
  .front .brand-name{font-size:40px;letter-spacing:-.5px}
  .front .brand-tag{font-size:13px;margin-top:4px}
  .front .quote-mark{left:42px;top:60px;font-size:96px;color:var(--paper)}
  .front .promise{left:40px;top:150px;width:170px;font-size:17.5px;line-height:25.3px;font-weight:500;font-style:italic;color:var(--paper);letter-spacing:.3px}
  .front .info{left:0;top:380px;width:458px;height:228px}
  .front .intro{left:40px;top:40px;width:380px;font-size:13px;line-height:17px;color:var(--paper)}
  .front .range{left:40px;top:110px;width:380px;font-size:13px;line-height:17px;font-weight:700;font-style:italic;color:var(--paper)}
  .front .covered{left:40px;top:168px;font-size:27px}
  .front .web{left:0;top:608px;width:458px;height:44px;text-align:center;font-size:20px;font-weight:600;line-height:44px;letter-spacing:.3px}

  /* back */
  .back{left:613px}
  .back .frame{left:0;top:0}
  .back .panel{left:14px;top:16px;width:429px;height:434px;background:var(--paper)}
  .back .quote-mark{font-size:60px;color:var(--leaf)}
  .back .lead{left:39px;top:82px;width:215px;font-size:12.5px;line-height:14.8px}
  .back .pill{left:39px;top:139px;width:120px;height:21px;border-radius:11px;background:var(--leaf);color:var(--paper);font-size:13px;font-weight:600;text-align:center;line-height:21px}
  .back .order-url{left:40px;top:164px;font-size:12px;font-weight:500}
  .back .order-note{left:41px;top:182px;font-size:8.5px;font-style:italic}
  .back .eco{left:255px;top:270px;width:162px;font-size:12.5px;line-height:14.6px}
  .back .shop{left:14px;top:450px;width:429px;height:188px}
  .back .shop-title{left:25px;top:36px;font-size:30px}
  .back .shop-url{left:25px;top:80px;font-size:14px;font-weight:600;color:var(--paper)}
  .back .shop-note{left:25px;top:97px;font-size:9px;font-style:italic;color:var(--leaf)}
  .back .phone{left:25px;top:113px;font-size:18px;font-weight:600;color:var(--paper)}
  .back .phone-note{left:25px;top:137px;font-size:9px;font-style:italic;color:var(--leaf)}
</style>
</head>
<body>

<section class="flyer front">
  <svg class="abs hero-shape" width="458" height="380" viewBox="0 0 458 380">
    <defs>
      <linearGradient id="produce" x1="0" y1="0" x2="1" y2="1">
        <stop offset="0" stop-color="var(--produce-a)"/>
        <stop offset=".5" stop-color="var(--produce-b)"/>
        <stop offset="1" stop-color="#5d7a2c"/>
      </linearGradient>
    </defs>
    <polygon points="0,13 181,13 289,370 0,370" fill="var(--leaf)"/>
    <polygon role="img" aria-label="Photo of assorted fresh vegetables and fruit" points="221,112 458,112 458,370 279,370" fill="url(#produce)"/>
  </svg>

  <div class="abs brand">
    <div class="brand-name">Grubella</div>
    <div class="brand-tag">home delivery</div>
  </div>

  <div class="abs quote-mark">“</div>
  <p class="abs promise">Lovingly picked Kentish food safely delivered from our farm to your home by passionate local people who care.</p>

  <div class="abs info stripes">
    <p class="abs intro"><b>Grubella</b> brings you the very best producers and growers from <b>The Garden of England</b> to deliver you a delicious choice for all your dining needs.</p>
    <p class="abs range">From fresh produce boxes, handmade picnic boxes, fresh Kentish berry boxes to the finest local beer and wines –</p>
    <p class="abs script covered">we’ve got it covered.</p>
  </div>

  <div class="abs web">www.grubellahomedelivery.example</div>
</section>

<section class="flyer back">
  <svg class="abs frame" width="459" height="652" viewBox="0 0 459 652">
    <rect width="459" height="652" fill="var(--leaf)"/>
    <polygon points="0,0 459,0 459,16 14,16 14,350 0,360" fill="var(--forest)"/>
  </svg>

  <div class="abs panel"></div>

  <svg class="abs" width="459" height="652" viewBox="0 0 459 652">
    <circle cx="372" cy="112" r="98" fill="none" stroke="var(--leaf)" stroke-width="2"/>
    <circle role="img" aria-label="Photo of bruschetta topped with tomato, olives and herbs" cx="376" cy="108" r="92" fill="#c96a4a"/>
    <circle cx="132" cy="315" r="93" fill="none" stroke="var(--leaf)" stroke-width="2"/>
    <circle role="img" aria-label="Photo of a picnic box with savoury bakes and salad" cx="132" cy="315" r="86" fill="#7d8a45"/>
    <ellipse role="img" aria-label="Photo of a fresh lettuce" cx="78" cy="410" rx="46" ry="38" fill="#4f9a2c"/>
    <ellipse role="img" aria-label="Photo of a red chilli pepper" cx="352" cy="412" rx="64" ry="12" transform="rotate(-20 352 412)" fill="#b52a1a"/>
    <circle cx="342" cy="540" r="72" fill="var(--paper)"/>
    <circle role="img" aria-label="Photo of a pizza topped with tomato and basil" cx="342" cy="540" r="65" fill="#c8572e"/>
  </svg>

  <div class="abs quote-mark" style="left:38px;top:38px">“</div>
  <p class="abs lead">Avoid the supermarkets and enjoy a unique and balanced food experience with provenance.</p>
  <div class="abs pill">Order online at</div>
  <div class="abs order-url">www.grubellahomedelivery.example</div>
  <div class="abs order-note">for fast contactless next day delivery.</div>

  <div class="abs quote-mark" style="left:252px;top:224px">“</div>
  <p class="abs eco">Using environmentally conscious practices and minimal packaging, working hand in hand with reduced food miles brings you peace of mind with our efforts for a sustainable future.</p>

  <div class="abs shop stripes">
    <div class="abs script shop-title">Shop Now At</div>
    <div class="abs shop-url">www.grubellahomedelivery.example</div>
    <div class="abs shop-note">or call one of our friendly team at the farm on</div>
    <div class="abs phone">01632 960418</div>
    <div class="abs phone-note">Start enjoying food with provenance now.</div>
  </div>
</section>

</body>
</html>
```